Penny Parcel Ad

I need to create a layout with the information on the PDF, but I want you to re-design it and freshen up the look. I've attached a Word Doc with the size and format requirement for the penny parcel print. The PDF I created in illustrator CS6 also has the proper guides.

Target Market(s)

Storm Damaged Areas

Font styles to use
Serif
Sans Serif

Requirements
Must have
• Fresh, clean design. I prefer upscale look versus modern or techy.

```html
<!DOCTYPE html>
<html lang="en">
<head>
<meta charset="utf-8">
<title>Fair Hands – Penny Parcel Ad</title>
<link rel="stylesheet" href="https://fonts.googleapis.com/css2?family=Anton&family=Barlow:wght@500;600;700;800&family=Barlow+Condensed:wght@400;500;600&display=swap">
<style>
  :root{
    --ink:#231f20;
    --brown:#3a2016;
    --orange:#e2711d;
    --roof:#8f9093;
    --wall:#fce9a0;
    --siding:#f1cf58;
    --panel:#fdf6dc;
    --guide:#000000;
    --paper:#ffffff;
    --c-grey:#9a9b9e;
    --c-yellow:#f5bf17;
    --c-orange:#e4702a;
    --c-red:#e21b3a;
  }
  *{box-sizing:border-box;margin:0;padding:0}
  html,body{width:1200px;height:777px;overflow:hidden;background:var(--guide)}
  .ad{position:relative;width:1200px;height:777px;background:var(--guide);font-family:"Barlow",sans-serif;color:var(--ink)}
  .guide-label{position:absolute;color:var(--orange);font:700 17px/1 "Barlow",sans-serif;letter-spacing:.5px}
  .guide-label.top{top:14px}
  .guide-label.bottom{top:745px}
  .guide-label.side{transform:rotate(-90deg);transform-origin:center}
  .guide-label.side.right{transform:rotate(90deg)}
  .sheet{position:absolute;left:35px;top:49px;width:1130px;height:679px;background:var(--paper);overflow:hidden}
  .house{position:absolute;left:0;top:0}
  .headline{position:absolute;left:24px;top:46px;font:800 62px/1 "Barlow",sans-serif;letter-spacing:.3px;color:var(--ink)}
  .url{position:absolute;left:29px;top:104px;font:700 31px/1 "Barlow",sans-serif;color:var(--ink)}
  .url span{color:var(--orange)}
  .badge-partner{position:absolute;left:957px;top:19px;width:152px;height:44px;background:#e0e0e0;border-radius:3px}
  .badge-partner::before{content:"";position:absolute;left:0;top:0;width:44px;height:44px;background:#d8262e;border-radius:3px}
  .badge-listing{position:absolute;left:959px;top:76px;width:108px;height:40px;background:var(--ink);border-radius:5px}
  .badge-grade{position:absolute;left:1082px;top:85px;width:24px;height:24px;background:var(--ink);border-radius:50%}
  .brand{position:absolute;left:619px;top:178px;display:flex;align-items:center;gap:14px}
  .brand-mark{width:84px;height:84px;border-radius:50%;background:radial-gradient(circle,#e7a63a 0%,#7a4a24 70%,var(--brown) 100%)}
  .brand-name{font:800 70px/1 "Barlow",sans-serif;color:var(--brown);letter-spacing:-1px}
  .phone{position:absolute;left:666px;top:258px;font:700 48px/1 "Barlow",sans-serif;color:var(--orange);letter-spacing:1px}
  .features{position:absolute;left:107px;top:341px;width:592px;height:184px;background:var(--panel);padding:12px 0 0 15px;display:grid;grid-template-columns:286px 290px;row-gap:20px}
  .feature h3{font:700 17px/18px "Barlow",sans-serif;color:var(--orange);text-transform:uppercase;letter-spacing:.3px}
  .feature p{margin-top:4px;font:600 14.5px/16px "Barlow",sans-serif;color:var(--ink)}
  .review{position:absolute;left:723px;top:341px;width:373px;height:184px;background:var(--panel);padding:9px 12px 0 12px}
  .review h3{font:700 14.5px/16px "Barlow",sans-serif;text-transform:uppercase;letter-spacing:.2px}
  .review p{margin-top:4px;padding-left:2px;font:400 11.8px/13.8px "Barlow Condensed",sans-serif;color:var(--ink)}
  .review cite{display:block;text-align:right;padding-right:7px;margin-top:1px;font:700 14px/16px "Barlow",sans-serif;font-style:normal}
  .coupons{position:absolute;left:0;top:545px;width:1130px;height:134px;display:flex}
  .coupon{position:relative;width:282.5px;height:134px;color:#111}
  .coupon.grey{background:var(--c-grey)}
  .coupon.yellow{background:var(--c-yellow)}
  .coupon.orange{background:var(--c-orange)}
  .coupon.red{background:var(--c-red)}
  .coupon-tag{position:absolute;left:14px;bottom:14px;transform:rotate(-90deg);transform-origin:left bottom;width:110px;height:80px}
  .coupon-tag strong{position:absolute;left:0;bottom:-30px;font:400 32px/1 "Anton",sans-serif;letter-spacing:.5px}
  .coupon-tag small{position:absolute;left:0;bottom:-70px;font:400 15px/15px "Barlow",sans-serif;width:130px}
  .coupon-rule{position:absolute;left:91px;top:14px;width:5px;height:109px;background:#111}
  .coupon-save{position:absolute;left:104px;top:12px;width:170px;text-align:center;font:400 40px/1 "Anton",sans-serif;letter-spacing:.5px;white-space:nowrap}
  .coupon-save .star{font-family:"Barlow",sans-serif;font-size:30px;vertical-align:6px}
  .coupon-value{position:absolute;left:104px;top:52px;width:170px;text-align:center;font:400 72px/1 "Anton",sans-serif}
</style>
</head>
<body>
<div class="ad">
  <span class="guide-label top" style="left:285px">margin</span>
  <span class="guide-label top" style="left:847px">margin</span>
  <span class="guide-label bottom" style="left:285px">margin</span>
  <span class="guide-label bottom" style="left:847px">margin</span>
  <span class="guide-label side" style="left:-7px;top:202px">margin</span>
  <span class="guide-label side" style="left:-7px;top:546px">margin</span>
  <span class="guide-label side right" style="left:1153px;top:202px">margin</span>
  <span class="guide-label side right" style="left:1153px;top:546px">margin</span>

  <div class="sheet">
    <svg class="house" width="1130" height="679" viewBox="0 0 1130 679" aria-hidden="true">
      <defs>
        <linearGradient id="eaveShadow" x1="0" y1="0" x2="0" y2="1">
          <stop offset="0" stop-color="#a6873c" stop-opacity=".55"/>
          <stop offset="1" stop-color="#fce9a0" stop-opacity="0"/>
        </linearGradient>
      </defs>
      <polygon points="77,323 817,91 1130,183 1130,545 77,545" fill="var(--wall)"/>
      <g stroke="var(--siding)" stroke-width="2">
        <line x1="77" y1="372" x2="1130" y2="372"/>
        <line x1="77" y1="407" x2="1130" y2="407"/>
        <line x1="77" y1="442" x2="1130" y2="442"/>
        <line x1="77" y1="477" x2="1130" y2="477"/>
        <line x1="77" y1="512" x2="1130" y2="512"/>
        <line x1="77" y1="337" x2="1130" y2="337"/>
        <line x1="600" y1="302" x2="1130" y2="302"/>
        <line x1="700" y1="267" x2="1130" y2="267"/>
        <line x1="820" y1="232" x2="1130" y2="232"/>
      </g>
      <polygon points="77,323 817,91 1130,183 1130,200 817,108 77,340" fill="url(#eaveShadow)"/>
      <polygon points="0,321 817,73 1130,166 1130,183 817,91 77,323 77,321" fill="var(--roof)"/>
    </svg>

    <h1 class="headline">Get a roof quote online!</h1>
    <p class="url">www.fairhandsgc.com/<span>roofquote</span></p>

    <div class="badge-partner" role="img" aria-label="Preferred contractor certification badge"></div>
    <div class="badge-listing" role="img" aria-label="Accredited business listing badge"></div>
    <div class="badge-grade" role="img" aria-label="Business rating badge"></div>

    <div class="brand">
      <span class="brand-name">Fair</span>
      <span class="brand-mark" role="img" aria-label="Company emblem with roofing crew"></span>
      <span class="brand-name">Hands</span>
    </div>
    <p class="phone">972 555 0148</p>

    <section class="features">
      <div class="feature">
        <h3>Fully insured<br>roofing crews</h3>
        <p>We carry both Liability Coverage &amp;<br>Workers Compensation for our crew.</p>
      </div>
      <div class="feature">
        <h3>Licensed Texas<br>property adjusters</h3>
        <p>We have experience adjusting claims &amp;<br>will help you close your claim quickly.</p>
      </div>
      <div class="feature">
        <h3>Quality, hand<br>nailed roofs</h3>
        <p>Ask about our professional<br>installation process.</p>
      </div>
      <div class="feature">
        <h3>Locally owned company<br>servicing North Texas</h3>
      </div>
    </section>

    <section class="review">
      <h3>See what your neighbors in North<br>Texas are saying about us</h3>
      <p>I am a very skeptical person when it comes to general contracting and particularly roofing. Fair Hands put the roof on my other-in-law's house after the last bad hail storm we had. Dan was at the work site about 90% of the time making sure he was available to not only the crew, but to my mother-in-law as well. He worked well with insurance adjuster and made sure all the paperwork was in order for the insurance company AND the bank. You just don't see service like that often. He went on to do my neighbor's house as well. Both jobs were done professionally and looked amazing. As long as Fair Hands is in business, I will continue to refer and use them.</p>
      <cite>Martin R - Decatur, TX</cite>
    </section>

    <div class="coupons">
      <div class="coupon grey">
        <div class="coupon-tag"><strong>COUPON</strong><small>on lorem ipsum<br>dolor consectatir</small></div>
        <span class="coupon-rule"></span>
        <p class="coupon-save"><span class="star">★</span> SAVE <span class="star">★</span></p>
        <p class="coupon-value">15%</p>
      </div>
      <div class="coupon yellow">
        <div class="coupon-tag"><strong>COUPON</strong><small>on lorem ipsum<br>dolor consectatir</small></div>
        <span class="coupon-rule"></span>
        <p class="coupon-save"><span class="star">★</span> SAVE <span class="star">★</span></p>
        <p class="coupon-value">25%</p>
      </div>
      <div class="coupon orange">
        <div class="coupon-tag"><strong>COUPON</strong><small>on lorem ipsum<br>dolor consectatir</small></div>
        <span class="coupon-rule"></span>
        <p class="coupon-save"><span class="star">★</span> SAVE <span class="star">★</span></p>
        <p class="coupon-value">30%</p>
      </div>
      <div class="coupon red">
        <div class="coupon-tag"><strong>COUPON</strong><small>on lorem ipsum<br>dolor consectatir</small></div>
        <span class="coupon-rule"></span>
        <p class="coupon-save"><span class="star">★</span> SAVE <span class="star">★</span></p>
        <p class="coupon-value">50%</p>
      </div>
    </div>
  </div>
</div>
</body>
</html>
```